Dorian Walsby Psychotherapy Business Card Design Project

I need a welcoming business card for a Somatic Psychotherapy private practice based in Melbourne, Australia. I help individual clients to work through issues in their life that are inhibiting achieving their full potential. I would like a san serif font and the oculars are:
blue: R:37 G:61 B:95 C:93 M:77 Y:38 K:28
orange: R:241 G:103 B:43 C:0 M:74 Y:93 K:0
The final design should communicate warm, welcoming and safe environment in which clients are supported to grow. It should also convey a collaborative approach to achieve success between me (the therapist) and the client. The uploaded file is my new logo. Also an organic look and feel while maintaining professionalism and a clean, simple look is sought after.
In addition to the logo my details are:
Dorian Walsby
Psychotherapist
B.Arts., Grad Dip. T&D., Dip.Som.Psych, MRKTA, MLOHVB
0417 582 930
dwalsby@dorianwalsby.com.au
www.dorianwalsby.com.au
Target Market(s)
Psychotherapy Clients
Industry/Entity Type
Environment

```html
<!DOCTYPE html>
<html lang="en">
<head>
<meta charset="utf-8">
<title>Dorian Walsby Psychotherapy – Business Card</title>
<link rel="stylesheet" href="https://fonts.googleapis.com/css2?family=Arimo:wght@400;700&display=swap">
<style>
  :root {
    --blue: #253d5f;
    --orange: #f1672b;
    --white: #ffffff;
    --rule: #d4d8de;
    --shadow: rgba(37, 61, 95, 0.22);
  }
  html, body {
    margin: 0;
    padding: 0;
    overflow: hidden;
    background: var(--white);
  }
  .card {
    position: relative;
    width: 1200px;
    height: 686px;
    background: var(--white);
    overflow: hidden;
    font-family: "Arimo", Arial, sans-serif;
    color: var(--blue);
  }
  .brand {
    position: absolute;
    left: 52px;
    top: 40px;
    display: flex;
    align-items: center;
    gap: 22px;
  }
  .brand-dot {
    width: 96px;
    height: 96px;
    border-radius: 50%;
    background: var(--orange);
  }
  .brand-name {
    font-weight: 700;
    font-size: 40px;
    color: var(--blue);
    letter-spacing: -0.3px;
  }
  .credentials {
    position: absolute;
    left: 48px;
    top: 206px;
    margin: 0;
    padding: 0;
    list-style: none;
    font-size: 37px;
    line-height: 51px;
    color: var(--blue);
  }
  .identity {
    position: absolute;
    left: 649px;
    top: 228px;
    width: 446px;
    text-align: center;
  }
  .identity-name {
    margin: 0;
    font-weight: 700;
    font-size: 64px;
    line-height: 72px;
    color: var(--blue);
    white-space: nowrap;
    margin-left: -40px;
    margin-right: -40px;
  }
  .identity-role {
    margin: 0;
    font-weight: 700;
    font-size: 38px;
    line-height: 44px;
    color: var(--orange);
  }
  .identity-rule {
    margin: 16px 0 0;
    height: 2px;
    border: 0;
    background: var(--rule);
  }
  .identity-shadow {
    position: absolute;
    left: 640px;
    top: 330px;
    width: 470px;
    height: 120px;
    background: radial-gradient(ellipse 50% 40% at 50% 35%, var(--shadow), rgba(37, 61, 95, 0) 100%);
    pointer-events: none;
  }
  .accent-strip {
    position: absolute;
    left: 0;
    top: 566px;
    width: 1200px;
    height: 15px;
    background: var(--orange);
  }
  .contact-band {
    position: absolute;
    left: 0;
    top: 581px;
    width: 1200px;
    height: 105px;
    background: var(--blue);
    color: var(--white);
  }
  .phone {
    position: absolute;
    left: 15px;
    top: 21px;
    display: flex;
    align-items: center;
    gap: 22px;
    font-size: 39px;
  }
  .phone-icon {
    width: 63px;
    height: 63px;
    border-radius: 8px;
    background: var(--orange);
    display: flex;
    align-items: center;
    justify-content: center;
  }
  .website {
    position: absolute;
    right: 30px;
    top: 32px;
    font-size: 35px;
    color: var(--white);
  }
  .website-domain {
    color: var(--orange);
  }
</style>
</head>
<body>
  <main class="card">
    <header class="brand">
      <span class="brand-dot"></span>
      <span class="brand-name">Dorian Walsby Psychotherapy</span>
    </header>

    <ul class="credentials">
      <li>B.Arts.</li>
      <li>Grad Dip. T&amp;D.</li>
      <li>Dip.Som.Psych</li>
      <li>MRKTA</li>
      <li>MLOHVB</li>
    </ul>

    <div class="identity-shadow"></div>
    <section class="identity">
      <h1 class="identity-name">Dorian Walsby</h1>
      <p class="identity-role">Psychotherapist</p>
      <hr class="identity-rule">
    </section>

    <div class="accent-strip"></div>
    <footer class="contact-band">
      <div class="phone">
        <span class="phone-icon">
          <svg width="40" height="40" viewBox="0 0 24 24" aria-hidden="true">
            <path fill="#ffffff" d="M6.6 10.8c1.4 2.8 3.8 5.1 6.6 6.6l2.2-2.2c.3-.3.7-.4 1-.2 1.1.4 2.3.6 3.6.6.6 0 1 .4 1 1V20c0 .6-.4 1-1 1C10.6 21 3 13.4 3 4c0-.6.4-1 1-1h3.5c.6 0 1 .4 1 1 0 1.3.2 2.5.6 3.6.1.3 0 .7-.2 1l-2.3 2.2z"/>
          </svg>
        </span>
        <span class="phone-number">0417 582 930</span>
      </div>
      <div class="website">www.<span class="website-domain">dorianwalsby</span>.com.au</div>
    </footer>
  </main>
</body>
</html>
```